Business start up

I need a logo within the business cards that has the name brixol with two racing stripes like the halvor racing stripes next to the name .... one of the stripes I would want to have the shades of window tint and the other stripe the colors of vinyl wrap or even the name having dripping paint of the different colors in it ... it will be a business of window tint and vinyl wrap .... service that I will be providing would be window tint Vinyl wrap Paint protection (ppfTaillights/headlights tintsBlackouts/Chrome delete Decals

Target Market(s)

Automotive

Industry/Entity Type

Automotive

Contact Information for Business Card

Have the name brixo drip like paint and have different colors dripping

Font styles to use
Serif
Sans Serif
Decorative
Script

Colors

Designer to choose colors to be used in the design.

Requirements
Nice to have
• I need a logo within the business cards that has the name brixol with two racing stripes like the halvor racing stripes next to the name .... one of the stripes I would want to have the shades of window tint and the other stripe the colors of vinyl wrap or even the name having dripping paint of the different colors in it ... it will be a business of window tint and vinyl wrap .... service that I will be providing would be
• window tint
• Vinyl wrap
• Paint protection (ppf
• Taillights/headlights tints
• Blackouts/Chrome delete
• Decals

```html
<!DOCTYPE html>
<html lang="en">
<head>
<meta charset="utf-8">
<title>Brixol Business Card</title>
<link href="https://fonts.googleapis.com/css2?family=Lato:wght@400;700;900&display=swap" rel="stylesheet">
<style>
  :root {
    --page-bg: #e9e7e3;
    --card-front: #ffffff;
    --card-back: #0f0f0f;
    --ink: #1a1a1a;
    --ink-soft: #3a3a3a;
    --divider: #555555;
    --mark-grey: #9a9a9a;
    --list-ink: #ffffff;
    --shadow: rgba(0, 0, 0, 0.45);
  }
  * { box-sizing: border-box; margin: 0; padding: 0; }
  html, body {
    width: 1200px; height: 1023px; overflow: hidden;
    background: var(--page-bg);
    font-family: "Lato", Arial, sans-serif;
  }
  .canvas { position: relative; width: 1200px; height: 1023px; }

  .card {
    position: absolute; left: 248px; width: 681px;
    box-shadow: -6px 6px 0 var(--shadow), 0 4px 10px rgba(0,0,0,.25);
  }
  .card--front { top: 87px; height: 390px; background: var(--card-front); }
  .card--back  { top: 542px; height: 388px; background: var(--card-back); }

  .brand {
    position: absolute; display: flex; align-items: center; gap: 12px;
    font-weight: 900; letter-spacing: 2px; font-size: 38px;
  }
  .brand__dot { width: 18px; height: 18px; border-radius: 50%; }
  .card--front .brand { left: 103px; top: 172px; color: var(--ink); }
  .card--front .brand__dot { background: var(--ink); }
  .card--back .brand { left: 40px; top: 167px; color: var(--mark-grey); }
  .card--back .brand__dot { background: var(--mark-grey); }

  .divider {
    position: absolute; left: 340px; top: 117px;
    width: 1px; height: 155px; background: var(--divider);
  }
  .person { position: absolute; left: 367px; top: 118px; color: var(--ink); }
  .person__name { font-size: 30px; font-weight: 900; line-height: 1; }
  .person__title { margin-top: 10px; font-size: 15.5px; color: var(--ink-soft); }

  .contact { position: absolute; left: 367px; top: 197px; list-style: none; }
  .contact__item {
    display: flex; align-items: center; height: 27px;
    font-size: 15.5px; color: var(--ink-soft);
  }
  .contact__icon { width: 14px; height: 14px; margin-right: 12px; fill: var(--ink); }

  .services {
    position: absolute; left: 308px; top: 87px; list-style: none;
    color: var(--list-ink); font-size: 26px; line-height: 42px;
  }
  .services__item { display: flex; align-items: center; }
  .services__item::before {
    content: ""; width: 12px; height: 12px; border-radius: 50%;
    background: var(--list-ink); margin-right: 20px;
  }
</style>
</head>
<body>
<main class="canvas">
  <section class="card card--front">
    <div class="brand"><span class="brand__dot"></span>BRIXOL</div>
    <div class="divider"></div>
    <div class="person">
      <h1 class="person__name">Owen Carter</h1>
      <p class="person__title">Founder &amp; CEO</p>
    </div>
    <ul class="contact">
      <li class="contact__item">
        <svg class="contact__icon" viewBox="0 0 24 24"><path d="M6.6 10.8a15 15 0 0 0 6.6 6.6l2.2-2.2c.3-.3.7-.4 1-.2 1.1.4 2.3.6 3.6.6.6 0 1 .4 1 1V20c0 .6-.4 1-1 1A17 17 0 0 1 3 4c0-.6.4-1 1-1h3.5c.6 0 1 .4 1 1 0 1.3.2 2.5.6 3.6.1.3 0 .7-.2 1z"/></svg>
        (555) 014/2288
      </li>
      <li class="contact__item">
        <svg class="contact__icon" viewBox="0 0 24 24"><path d="M2 5h20v14H2zM4 7v.4l8 5.6 8-5.6V7zm0 2.8V17h16V9.8l-8 5.6z"/></svg>
        info@yourmail.com
      </li>
      <li class="contact__item">
        <svg class="contact__icon" viewBox="0 0 24 24"><path d="M12 2a10 10 0 1 0 0 20 10 10 0 0 0 0-20zm0 2c.9 0 2.2 1.8 2.7 5H9.3C9.8 5.8 11.1 4 12 4zm-3 .6A13 13 0 0 0 7.3 9H4.9A8 8 0 0 1 9 4.6zm6 0A8 8 0 0 1 19.1 9h-2.4A13 13 0 0 0 15 4.6zM4.3 11h2.8a17 17 0 0 0 0 2H4.3a8 8 0 0 1 0-2zm4.8 0h5.8a15 15 0 0 1 0 2H9.1a15 15 0 0 1 0-2zm7.8 0h2.8a8 8 0 0 1 0 2h-2.8a17 17 0 0 0 0-2zM4.9 15h2.4A13 13 0 0 0 9 19.4 8 8 0 0 1 4.9 15zm4.4 0h5.4c-.5 3.2-1.8 5-2.7 5s-2.2-1.8-2.7-5zm7.4 0h2.4a8 8 0 0 1-4.1 4.4 13 13 0 0 0 1.7-4.4z"/></svg>
        www.yourwebsite.com
      </li>
    </ul>
  </section>

  <section class="card card--back">
    <div class="brand"><span class="brand__dot"></span>BRIXOL</div>
    <ul class="services">
      <li class="services__item">window tint</li>
      <li class="services__item">Vinyl wrap</li>
      <li class="services__item">Paint protection (ppf)</li>
      <li class="services__item">Taillights/headlights tints</li>
      <li class="services__item">Blackouts/Chrome delete</li>
      <li class="services__item">Decals</li>
    </ul>
  </section>
</main>
</body>
</html>
```